I need a header for the web site www.harlowspipeworks.example/demo
It must include the following
Existig Logo (I will upload the .png)
Text: Serving Calgary and Surrounding Areas for Over 30 Years!
24 Hour Service
Call 403.718.2946 (Note this isn't the actual phone number I will need to be able to change the Phone number once the site is ready to put in a tracking number so I am hoping I get a PSD file with this where the text is editable)
We wnat the feel to be warm and geared more towards a residential customer rather than an industial customer.
We would like blue tones but are open to anything warm.

Size: Aprroximately 960x300

• Rounded Corners to match the content area on the site

```html
<!DOCTYPE html>
<html lang="en">
<head>
<meta charset="utf-8">
<title>Harlow's Pipeworks — Header</title>
<link href="https://fonts.googleapis.com/css2?family=Arimo:wght@400;700&display=swap" rel="stylesheet">
<style>
  :root {
    --page-bg: #ffffff;
    --banner-top: #f1f3f6;
    --banner-upper: #dfe5ed;
    --banner-mid: #8ea4c4;
    --banner-low: #2f4f86;
    --banner-bottom: #0c2558;
    --banner-edge: #b9c3d1;
    --brand-ink: #1d2a44;
    --tagline-orange: #f7a21b;
    --service-white: #eef2f8;
  }

  html, body {
    margin: 0;
    padding: 0;
    width: 1200px;
    height: 375px;
    overflow: hidden;
    background: var(--page-bg);
  }

  .header-canvas {
    position: relative;
    width: 1200px;
    height: 375px;
  }

  .header-banner {
    position: absolute;
    left: 6px;
    top: 10px;
    width: 1188px;
    height: 352px;
    border-radius: 14px;
    overflow: hidden;
    background: linear-gradient(
      to bottom,
      var(--banner-top) 0%,
      var(--banner-upper) 28%,
      var(--banner-mid) 58%,
      var(--banner-low) 80%,
      var(--banner-bottom) 100%
    );
    box-shadow: 0 0 0 1px var(--banner-edge), 0 2px 5px rgba(0, 0, 0, 0.25);
  }

  .blueprint-backdrop {
    position: absolute;
    left: 60px;
    top: 0;
    width: 1070px;
    height: 230px;
    background: radial-gradient(ellipse at center, rgba(255, 255, 255, 0.35) 0%, rgba(255, 255, 255, 0) 70%);
  }

  .brand-name {
    position: absolute;
    left: 0;
    right: 0;
    top: 62px;
    margin: 0;
    text-align: center;
    font-family: "Arimo", Arial, sans-serif;
    font-weight: 700;
    font-size: 46px;
    letter-spacing: 4px;
    color: var(--brand-ink);
    text-transform: uppercase;
  }

  .service-area {
    position: absolute;
    left: 0;
    right: 0;
    top: 266px;
    margin: 0;
    text-align: center;
    font-family: "Arimo", Arial, sans-serif;
    font-weight: 700;
    font-size: 25px;
    letter-spacing: 1.6px;
    color: var(--tagline-orange);
    text-transform: uppercase;
  }

  .contact-line {
    position: absolute;
    left: 0;
    right: 0;
    top: 308px;
    margin: 0;
    text-align: center;
    font-family: "Arimo", Arial, sans-serif;
    font-weight: 400;
    font-size: 27px;
    letter-spacing: 2.4px;
    color: var(--service-white);
    text-transform: uppercase;
  }

  .contact-divider {
    display: inline-block;
    margin: 0 34px;
  }
</style>
</head>
<body>
  <div class="header-canvas">
    <header class="header-banner">
      <div class="blueprint-backdrop" role="img" aria-label="Faint plumbing blueprint drawing in the background"></div>
      <h1 class="brand-name">Harlow's Pipeworks</h1>
      <p class="service-area">Serving Calgary and Surrounding Areas for Over 30 Years!</p>
      <p class="contact-line">
        <span class="service-hours">24 Hour Service</span><span class="contact-divider">|</span><span class="service-phone">Call 403.718.2946</span>
      </p>
    </header>
  </div>
</body>
</html>
```